" Prestamos serviços de suporte técnico à clientes como: -gestão de TI, -instalação de rede, firewall, internet/intranet -Segurança da Informação -Auditoria de Parque de Equipamentos de TI e Segurança de dados "

```html
<!DOCTYPE html>
<html lang="pt-BR">
<head>
<meta charset="utf-8">
<title>Papel Timbrado – Vertente & Horizontes</title>
<link href="https://fonts.googleapis.com/css2?family=Montserrat:wght@400;500;800&display=swap" rel="stylesheet">
<style>
  :root {
    --backdrop: #e4e6ea;
    --paper: #ffffff;
    --navy: #1e2a46;
    --blue: #2b8ed6;
    --blue-deep: #1a63a8;
    --blue-light: #7cc2f0;
    --watermark: #e6e7e9;
    --text: #4a4f5a;
  }
  * { margin: 0; padding: 0; box-sizing: border-box; }
  html, body {
    width: 1200px; height: 1200px; overflow: hidden;
    background: var(--backdrop);
    font-family: "Montserrat", sans-serif;
  }
  .letterhead {
    position: absolute;
    left: 211px; top: 50px;
    width: 778px; height: 1100px;
    background: var(--paper);
    box-shadow: 0 6px 24px rgba(0,0,0,0.12);
  }
  .brand {
    position: absolute; top: 52px; left: 0; width: 100%;
    display: flex; align-items: center; justify-content: center; gap: 10px;
  }
  .brand-mark {
    width: 14px; height: 14px; border-radius: 50%;
    background: var(--blue);
  }
  .brand-name {
    font-weight: 800; font-size: 22px; color: var(--navy);
    letter-spacing: 0.5px;
  }
  .watermark {
    position: absolute; top: 470px; left: 0; width: 100%;
    display: flex; align-items: center; justify-content: center; gap: 22px;
  }
  .watermark-mark {
    width: 44px; height: 44px; border-radius: 50%;
    background: var(--watermark);
  }
  .watermark-name {
    font-weight: 800; font-size: 50px; color: var(--watermark);
    letter-spacing: 1px;
  }
  .contact {
    position: absolute; left: 0; width: 100%; top: 1000px;
    font-size: 11px; color: var(--text); font-weight: 500;
  }
  .contact-row {
    display: flex; justify-content: center; align-items: center; gap: 16px;
  }
  .contact-item { display: flex; align-items: center; gap: 5px; }
  .contact-item svg { width: 12px; height: 12px; fill: var(--blue); }
  .address {
    margin-top: 10px;
    display: flex; justify-content: center; align-items: flex-start; gap: 6px;
    line-height: 1.35;
  }
  .address svg { width: 12px; height: 14px; fill: var(--blue); margin-top: 2px; }
  .footer-band {
    position: absolute; left: 0; bottom: 28px; width: 100%; height: 9px;
    background: linear-gradient(90deg, var(--blue-light), var(--blue) 45%, var(--blue-deep));
  }
</style>
</head>
<body>
  <main class="letterhead">
    <header class="brand">
      <span class="brand-mark"></span>
      <span class="brand-name">Vertente &amp; Horizontes</span>
    </header>

    <div class="watermark" aria-hidden="true">
      <span class="watermark-mark"></span>
      <span class="watermark-name">Vertente &amp; Horizontes</span>
    </div>

    <footer class="contact">
      <div class="contact-row">
        <span class="contact-item">
          <svg viewBox="0 0 24 24"><path d="M6.6 10.8a15.5 15.5 0 0 0 6.6 6.6l2.2-2.2c.3-.3.7-.4 1-.2 1.1.4 2.3.6 3.6.6.6 0 1 .4 1 1V20c0 .6-.4 1-1 1A17 17 0 0 1 3 4c0-.6.4-1 1-1h3.5c.6 0 1 .4 1 1 0 1.3.2 2.5.6 3.6.1.3 0 .7-.2 1z"/></svg>
          (21) 9 4000-1234
        </span>
        <span class="contact-item">
          <svg viewBox="0 0 24 24"><path d="M6.6 10.8a15.5 15.5 0 0 0 6.6 6.6l2.2-2.2c.3-.3.7-.4 1-.2 1.1.4 2.3.6 3.6.6.6 0 1 .4 1 1V20c0 .6-.4 1-1 1A17 17 0 0 1 3 4c0-.6.4-1 1-1h3.5c.6 0 1 .4 1 1 0 1.3.2 2.5.6 3.6.1.3 0 .7-.2 1z"/></svg>
          (21) 3000-5678
        </span>
        <span class="contact-item">
          <svg viewBox="0 0 24 24"><path d="M12 2a10 10 0 1 0 0 20 10 10 0 0 0 0-20zm6.9 6h-2.9a15.7 15.7 0 0 0-1.4-3.6A8 8 0 0 1 18.9 8zM12 4c.8 1.2 1.5 2.5 1.9 4h-3.8c.4-1.5 1.1-2.8 1.9-4zM4.3 14a8 8 0 0 1 0-4h3.4a16 16 0 0 0 0 4zm.8 2h2.9c.3 1.3.8 2.5 1.4 3.6A8 8 0 0 1 5.1 16zM8 8H5.1a8 8 0 0 1 4.3-3.6C8.8 5.5 8.3 6.7 8 8zm4 12c-.8-1.2-1.5-2.5-1.9-4h3.8c-.4 1.5-1.1 2.8-1.9 4zm2.3-6H9.7a14.7 14.7 0 0 1 0-4h4.6a14.7 14.7 0 0 1 0 4zm.3 5.6c.6-1.1 1.1-2.3 1.4-3.6h2.9a8 8 0 0 1-4.3 3.6zm1.7-5.6a16 16 0 0 0 0-4h3.4a8 8 0 0 1 0 4z"/></svg>
          www.vertentehorizontes.com.br
        </span>
      </div>
      <div class="address">
        <svg viewBox="0 0 20 24"><path d="M10 0a8 8 0 0 0-8 8c0 6 8 16 8 16s8-10 8-16a8 8 0 0 0-8-8zm0 11a3 3 0 1 1 0-6 3 3 0 0 1 0 6z"/></svg>
        <span>Rua das Palmeiras, 140 - Sala 802 - Centro<br>Rio de Janeiro/RJ - CEP: 20000-100</span>
      </div>
    </footer>

    <div class="footer-band"></div>
  </main>
</body>
</html>
```